Business Card for a Life Coaching Company

BRAVOPEAK is a Life Coaching company that was initiated to support people who want to transform thier life or ana aspect of it.
our slogan is : "Dream. Believe. Succeed"
our logo is uploaded.
The name of the company implies that leadership, strength and wisdom required to change your life.
We want an attractive business card that would give an impression of reliability, support and change. so we really want it unique. Here are some examples of unique cards:

http://www.cardcraftvault.example/2009/05/100-really-creative-business-cards/

BravoPeak is a life coaching organization focusing on individual transformation through the application of relevant and timeless principles of success.  BravoPeak believes that real, sustainable life transformations are brought about by tuning into the timeless wisdom we each carry in our hearts while boldy acting in the direction of our dreams.

Contacts on the card:
Address: 7 Tarek Nour El Dine Heliopolis Cairo Egypt
Tel: +202 24 71 38 52
Fax: +202 24 71 38 17
Mobile: +2 012 684 2097 (Dalia Soliman)
+2 0199915815 (Tariq Bhatti)

By the way, our temporary website is http://www.bravopeak.example

We have attached an .eps file with various configurations of our logo.

```html
<!DOCTYPE html>
<html lang="en">
<head>
<meta charset="utf-8">
<title>BravoPeak Business Card</title>
<link href="https://fonts.googleapis.com/css2?family=EB+Garamond:wght@400;500&family=Open+Sans:wght@700&display=swap" rel="stylesheet">
<style>
  :root {
    --page: #ffffff;
    --label: #8c8c8c;
    --orange-deep: #e8620f;
    --orange-mid: #f07a18;
    --orange-light: #f6a02c;
    --cream: #fdf8f0;
    --ink-grey: #7a7068;
    --ink-orange: #e0651c;
    --divider: #c9b9a8;
    --white: #ffffff;
    --web-tint: #fbd79a;
  }
  * { margin: 0; padding: 0; box-sizing: border-box; }
  html, body { width: 1200px; height: 873px; overflow: hidden; background: var(--page); }
  .canvas { position: relative; width: 1200px; height: 873px; }

  .side-label {
    position: absolute; left: 48px;
    font-family: "Open Sans", Arial, sans-serif; font-weight: 700;
    font-size: 60px; color: var(--label); line-height: 1;
  }
  .side-label--front { top: 157px; }
  .side-label--back { top: 548px; }

  .card {
    position: absolute; left: 312px; width: 642px; height: 366px;
    overflow: hidden; box-shadow: 0 2px 6px rgba(0,0,0,0.25);
    font-family: "EB Garamond", Georgia, serif;
  }
  .card--front { top: 37px; }
  .card--back { top: 440px; }

  .damask-field {
    position: absolute; inset: 0;
    background: radial-gradient(ellipse at 50% 40%, var(--orange-light) 0%, var(--orange-mid) 55%, var(--orange-deep) 100%);
  }

  .brand-mark {
    position: absolute; display: flex; align-items: center; gap: 8px;
    font-family: "EB Garamond", Georgia, serif; font-weight: 500;
    letter-spacing: 1px; line-height: 1; white-space: nowrap;
  }
  .brand-mark__dot { border-radius: 50%; flex: none; }

  .card--front .brand-mark { left: 34px; top: 312px; font-size: 21px; color: var(--white); }
  .card--front .brand-mark__dot { width: 15px; height: 15px; background: var(--white); }

  .slogan {
    position: absolute; left: 257px; top: 302px;
    font-size: 31px; line-height: 1.2; color: var(--white); white-space: nowrap;
  }

  .band { position: absolute; left: 0; right: 0; overflow: hidden; }
  .band--top { top: 0; height: 58px; }
  .band--bottom { top: 298px; height: 68px; }

  .info-panel {
    position: absolute; left: 0; right: 0; top: 58px; height: 240px;
    background: var(--cream);
  }
  .identity {
    position: absolute; left: 10px; top: 86px; width: 196px;
    display: flex; flex-direction: column; align-items: center; gap: 12px;
  }
  .card--back .brand-mark { position: static; font-size: 21px; color: var(--ink-orange); }
  .card--back .brand-mark__dot { width: 15px; height: 15px; background: var(--ink-orange); }

  .address {
    font-size: 12.5px; line-height: 17px; color: var(--ink-grey); text-align: center;
  }
  .divider {
    position: absolute; left: 218px; top: 76px; width: 1px; height: 108px;
    background: var(--divider);
  }
  .contacts {
    position: absolute; left: 288px; top: 70px;
    font-size: 16px; line-height: 28px; color: var(--ink-grey); list-style: none;
    white-space: nowrap;
  }
  .contacts .value { color: var(--ink-orange); }
  .contacts .indent { padding-left: 64px; }

  .website {
    position: absolute; left: 0; right: 0; top: 22px; text-align: center;
    font-size: 15px; letter-spacing: 9px; color: var(--web-tint);
  }
</style>
</head>
<body>
<main class="canvas">
  <div class="side-label side-label--front">Side 1</div>
  <section class="card card--front" aria-label="Business card front">
    <div class="damask-field" role="img" aria-label="Orange damask floral pattern background"></div>
    <div class="brand-mark"><span class="brand-mark__dot"></span>BRAVOPEAK</div>
    <p class="slogan">Dream. Believe. Succeed.</p>
  </section>

  <div class="side-label side-label--back">Side 2</div>
  <section class="card card--back" aria-label="Business card back">
    <div class="band band--top">
      <div class="damask-field" role="img" aria-label="Orange damask floral pattern band"></div>
    </div>
    <div class="info-panel">
      <div class="identity">
        <div class="brand-mark"><span class="brand-mark__dot"></span>BRAVOPEAK</div>
        <p class="address">7 Tarek Nour El Dine<br>Heliopolis Cairo Egypt</p>
      </div>
      <div class="divider"></div>
      <ul class="contacts">
        <li>Tel: <span class="value">+202 24 71 38 52</span></li>
        <li>Fax: <span class="value">+202 24 71 38 17</span></li>
        <li>Mobile: <span class="value">+2 012 684 2097 (Dalia Soliman)</span></li>
        <li class="indent"><span class="value">+2 0197328406 (Tariq Bhatti)</span></li>
      </ul>
    </div>
    <div class="band band--bottom">
      <div class="damask-field" role="img" aria-label="Orange damask floral pattern band"></div>
      <p class="website">www.bravopeak.example</p>
    </div>
  </section>
</main>
</body>
</html>
```